High-End Bifold Brochure for Aesthetics Medspa Business

I need a print-ready, bifold brochure designed for a high-end, luxurious Aesthetics/Medspa practice.

The brochure will showcase the latest IV Therapy content (6 options included in MENU.docx), and exclusive Vitamin B12+ wellness shot content (included in LS PDF). It should also include the business logo and basic office contact options.

The design should be clean, modern, and appealing with a light design. It should flow nicely and compliment the website theme/design. Preferably, having the 6 IV treatments inside bifold, with B12 shot on back/outside page. For easy viewing.

I have attached a few licensed images, if you think they will incorporate into the design nicely. Otherwise, please ignore them. If needed, I can send more.

https://lunavelleskincareclinic.com/
Brand purple: #491c64
Fonts used on site:
Josefin Sans
Montserrat

Size should be 6.5 x 9 using specs on Quillapress's template page (Half Fold design)
https://www.quillapress.com/resources/templates

• Montserrat, Josefin Sans, or similar

• Content included in MENU + B12 shot content on PDF.
Similar feel to the website, High-end, modern, luxurious

```html
<!DOCTYPE html>
<html lang="en">
<head>
<meta charset="utf-8">
<title>Lunavelle Skincare Clinic – IV Therapy Brochure</title>
<link href="https://fonts.googleapis.com/css2?family=Josefin+Sans:wght@400;600;700&family=Montserrat:wght@400;500;600;700&family=Oswald:wght@600&display=swap" rel="stylesheet">
<style>
:root{
  --purple:#491c64;
  --purple-mid:#5e2585;
  --purple-bright:#7b35a8;
  --orange:#f08a2c;
  --gold:#f7b45a;
  --ink:#1d1d1f;
  --text:#474747;
  --paper:#ffffff;
  --paper-shade:#f2f2f4;
  --backdrop:#6a6a6a;
}
*{box-sizing:border-box;margin:0;padding:0}
html,body{width:1200px;height:900px;overflow:hidden}
body{background:var(--backdrop);font-family:"Montserrat",sans-serif;color:var(--text);position:relative}

.spread{position:absolute;top:60px;width:564px;height:780px;box-shadow:0 18px 40px rgba(0,0,0,.35)}
.spread-outside{left:18px}
.spread-inside{left:618px;background:var(--paper);border-bottom:3px solid var(--purple-bright)}
.spread-art{position:absolute;inset:0;width:100%;height:100%}
.fold{position:absolute;top:0;bottom:0;left:282px;width:1px;background:rgba(0,0,0,.12)}

/* back panel */
.back-panel{position:absolute;left:0;top:0;width:282px;height:780px}
.cta{position:absolute;left:40px;top:40px}
.cta-line{font-family:"Josefin Sans",sans-serif;font-weight:700;font-size:16px;color:var(--ink);letter-spacing:.3px}
.cta-strong{font-family:"Oswald",sans-serif;font-weight:600;font-size:25px;color:var(--ink);line-height:1.05;letter-spacing:.2px}
.phone-pill{position:absolute;left:34px;top:96px;width:222px;height:28px;background:var(--purple);border-radius:14px;display:flex;align-items:center;padding-left:50px;color:#fff;font-family:"Josefin Sans",sans-serif;font-weight:700;font-size:17px;letter-spacing:.5px}
.phone-badge{position:absolute;left:0;top:-5px;width:38px;height:38px;border-radius:50%;background:#fff;border:2px solid var(--purple);display:flex;align-items:center;justify-content:center}
.contact{position:absolute;left:0;right:0;top:682px;text-align:center;color:#fff;font-size:10px;line-height:1.45}
.contact-email{margin-top:8px}
.socials{display:flex;justify-content:center;gap:6px;margin-top:9px}
.social-dot{width:16px;height:16px;border-radius:50%;background:#fff}

/* front panel */
.front-panel{position:absolute;left:282px;top:0;width:282px;height:780px}
.brand{position:absolute;left:24px;top:34px;display:flex;align-items:center;gap:10px}
.brand-mark{width:46px;height:46px;border-radius:50%;border:2px solid var(--purple)}
.brand-name{font-family:"Montserrat",sans-serif;font-weight:600;font-size:15px;line-height:1.15;color:var(--purple)}
.front-title{position:absolute;left:0;right:0;top:640px;text-align:center;color:#fff}
.front-city{font-family:"Josefin Sans",sans-serif;font-weight:700;font-size:40px;letter-spacing:1px;line-height:1}
.front-tag{font-family:"Josefin Sans",sans-serif;font-weight:700;font-size:20px;letter-spacing:1px;margin-top:4px}
.front-rule{width:90px;height:1px;background:rgba(255,255,255,.7);margin:12px auto 10px}
.front-web{font-size:10px;letter-spacing:.8px}
.front-web b{font-weight:600}

/* inside: menu */
.menu-panel{position:absolute;left:0;top:0;width:282px;height:780px;padding:28px 24px 18px 25px;display:flex;flex-direction:column}
.menu-title{font-family:"Josefin Sans",sans-serif;font-weight:700;font-size:20px;color:var(--ink);letter-spacing:.6px;line-height:1}
.menu-bar{background:var(--purple);color:#fff;font-family:"Josefin Sans",sans-serif;font-weight:700;font-size:18px;letter-spacing:5px;padding:4px 0 1px 36px;margin-top:3px}
.menu-list{flex:1;display:flex;flex-direction:column;justify-content:space-between;margin-top:18px}
.item-head{display:flex;align-items:flex-end;height:26px}
.item-name{font-family:"Josefin Sans",sans-serif;font-weight:600;font-size:11.5px;color:var(--purple);line-height:1.05;letter-spacing:.3px;white-space:nowrap}
.item-leader{flex:1;height:14px;margin-left:2px;min-width:20px}
.item-price{background:var(--purple);color:#fff;font-family:"Josefin Sans",sans-serif;font-weight:700;font-size:13px;padding:5px 8px 3px 16px;clip-path:polygon(10px 0,100% 0,100% 100%,0 100%);margin-bottom:-6px}
.item-desc{font-size:7.3px;line-height:1.3;color:var(--text);margin-top:10px;text-align:justify}

/* inside: vitamins */
.vitamin-panel{position:absolute;left:282px;top:0;width:282px;height:780px;padding:34px 22px 18px 24px}
.vit-title{font-family:"Josefin Sans",sans-serif;font-weight:700;font-size:19px;color:var(--ink);letter-spacing:.5px}
.vit-banner{background:var(--purple);color:#fff;font-family:"Josefin Sans",sans-serif;font-weight:700;font-size:10px;line-height:1.35;letter-spacing:.3px;padding:8px 10px 5px 12px;margin-top:2px;transform:skewY(-1.5deg)}
.nutrients{list-style:none;margin-top:14px}
.nutrient{display:flex;gap:7px;font-size:7.2px;line-height:1.35;margin-bottom:9px}
.nutrient svg{flex:none;margin-top:1px}
.nutrient b{color:var(--purple);font-weight:700}
.benefits-head{display:flex;align-items:flex-end;margin-top:18px}
.benefits-title{font-family:"Josefin Sans",sans-serif;font-weight:700;font-size:11.5px;color:var(--purple);letter-spacing:.4px;white-space:nowrap}
.benefits{list-style:none;margin-top:12px}
.benefit{display:flex;gap:8px;font-size:7.3px;line-height:1.35;margin-bottom:8px}
.benefit svg{flex:none;margin-top:1px}
</style>
</head>
<body>

<!-- Outside spread -->
<section class="spread spread-outside">
  <svg class="spread-art" viewBox="0 0 564 780" preserveAspectRatio="none" aria-hidden="false">
    <defs>
      <linearGradient id="photoTone" x1="0" y1="0" x2="1" y2="1">
        <stop offset="0" stop-color="#6f5f5a"/>
        <stop offset=".45" stop-color="#d8b9a6"/>
        <stop offset=".75" stop-color="#e9cdbb"/>
        <stop offset="1" stop-color="#9b8176"/>
      </linearGradient>
      <linearGradient id="clientTone" x1="0" y1="0" x2="1" y2="1">
        <stop offset="0" stop-color="#d9d6dc"/>
        <stop offset=".5" stop-color="#b0826a"/>
        <stop offset="1" stop-color="#3a2a30"/>
      </linearGradient>
      <linearGradient id="orangeWave" x1="0" y1="0" x2="1" y2="0">
        <stop offset="0" stop-color="var(--gold)"/>
        <stop offset=".55" stop-color="var(--orange)"/>
        <stop offset="1" stop-color="#e0732a"/>
      </linearGradient>
      <linearGradient id="purpleWave" x1="0" y1="0" x2="1" y2="0">
        <stop offset="0" stop-color="var(--purple-bright)"/>
        <stop offset=".5" stop-color="var(--purple-mid)"/>
        <stop offset="1" stop-color="var(--purple-bright)"/>
      </linearGradient>
    </defs>
    <rect width="564" height="780" fill="var(--paper)"/>
    <g role="img" aria-label="Photograph of a woman with radiant skin resting her hand at her temple">
      <rect x="0" y="110" width="564" height="580" fill="url(#photoTone)"/>
    </g>
    <path d="M0 0 H564 V150 C470 140 390 175 282 190 C180 205 70 190 0 128 Z" fill="var(--paper-shade)"/>
    <path d="M0 128 C70 190 180 205 282 190 C390 175 470 140 564 150 L564 162 C470 158 390 200 282 222 C180 240 80 215 0 160 Z" fill="url(#purpleWave)"/>
    <g role="img" aria-label="Photograph of a smiling client during an IV therapy treatment">
      <circle cx="96" cy="438" r="128" fill="url(#clientTone)" stroke="var(--purple)" stroke-width="7"/>
    </g>
    <path d="M0 660 C120 650 230 580 340 560 C430 545 510 580 564 640 L564 655 C510 600 430 568 340 582 C230 600 120 665 0 672 Z" fill="url(#orangeWave)"/>
    <path d="M0 672 C120 665 230 600 340 582 C430 568 510 600 564 655 V780 H0 Z" fill="var(--purple)"/>
  </svg>
  <div class="fold"></div>

  <div class="back-panel">
    <div class="cta">
      <p class="cta-line">CALL TODAY FOR YOUR</p>
      <p class="cta-strong">FREE CONSULTATION</p>
    </div>
    <div class="phone-pill">
      <span class="phone-badge">
        <svg width="18" height="18" viewBox="0 0 24 24" fill="none" stroke="var(--purple)" stroke-width="2" stroke-linecap="round" stroke-linejoin="round"><path d="M5 3h4l2 5-2.5 1.5a11 11 0 0 0 6 6L16 13l5 2v4a2 2 0 0 1-2 2A16 16 0 0 1 3 5a2 2 0 0 1 2-2z"/></svg>
      </span>
      (520) 555-0147
    </div>
    <div class="contact">
      <svg width="9" height="12" viewBox="0 0 12 16" fill="none" stroke="#fff" stroke-width="1.6"><path d="M6 15s5-5.5 5-9A5 5 0 0 0 1 6c0 3.5 5 9 5 9z"/><circle cx="6" cy="6" r="1.8"/></svg>
      <p>2280 N Saguaro Vista Rd, Suite 104<br>Tucson, Arizona 85718</p>
      <p class="contact-email">✉ info@lunavelleskincareclinic.com</p>
      <div class="socials"><span class="social-dot"></span><span class="social-dot"></span><span class="social-dot"></span><span class="social-dot"></span></div>
    </div>
  </div>

  <div class="front-panel">
    <div class="brand">
      <span class="brand-mark"></span>
      <p class="brand-name">LUNAVELLE SKINCARE<br>CLINIC</p>
    </div>
    <div class="front-title">
      <p class="front-city">TUCSON'S</p>
      <p class="front-tag">PREMIER MEDSPA</p>
      <div class="front-rule"></div>
      <p class="front-web">www.<b>LunavelleSkincareClinic</b>.com</p>
    </div>
  </div>
</section>

<!-- Inside spread -->
<section class="spread spread-inside">
  <div class="fold"></div>

  <div class="menu-panel">
    <h2 class="menu-title">THE INFUSION LOUNGE</h2>
    <p class="menu-bar">IV THERAPY</p>
    <div class="menu-list">
      <article class="menu-item">
        <div class="item-head"><h3 class="item-name">IMMUNITY BOOSTER</h3><svg class="item-leader" viewBox="0 0 100 14" preserveAspectRatio="none"><path d="M0 13 H72 L84 1 H100" fill="none" stroke="var(--purple)" stroke-width="1" vector-effect="non-scaling-stroke"/></svg><span class="item-price">$150</span></div>
        <p class="item-desc">Have a cold, flu or just need to give your immunity a boost? Let us mix a powerful punch in our booster bag just for you to prevent or relieve aches and pain</p>
      </article>
      <article class="menu-item">
        <div class="item-head"><h3 class="item-name">REFRESH &amp; HYDRATE</h3><svg class="item-leader" viewBox="0 0 100 14" preserveAspectRatio="none"><path d="M0 13 H72 L84 1 H100" fill="none" stroke="var(--purple)" stroke-width="1" vector-effect="non-scaling-stroke"/></svg><span class="item-price">$100</span></div>
        <p class="item-desc">Relieve dehydration from the extremes of lifestyle with our balanced electrolyte cocktail targeting jet lag, fatigue, stress and sports related activity to leave you feeling more youthful and refreshed!</p>
      </article>
      <article class="menu-item">
        <div class="item-head"><h3 class="item-name">MIGRAINE BUSTER</h3><svg class="item-leader" viewBox="0 0 100 14" preserveAspectRatio="none"><path d="M0 13 H72 L84 1 H100" fill="none" stroke="var(--purple)" stroke-width="1" vector-effect="non-scaling-stroke"/></svg><span class="item-price">$150</span></div>
        <p class="item-desc">Eradicate your migraine pain, nausea, vomiting, and light sensitivity with our magic formula</p>
      </article>
      <article class="menu-item">
        <div class="item-head"><h3 class="item-name">WELLNESS INFUSION:<br>Myer's Cocktail</h3><svg class="item-leader" viewBox="0 0 100 14" preserveAspectRatio="none"><path d="M0 13 H72 L84 1 H100" fill="none" stroke="var(--purple)" stroke-width="1" vector-effect="non-scaling-stroke"/></svg><span class="item-price">$180</span></div>
        <p class="item-desc">This infusion of vitamins, minerals and electrolytes results in direct access of these nutrients into your cells, enhancing energy, decreasing stress and anxiety in addition to improving memory. Other benefits include relief of asthma, depression, allergies and fibromyalgia pain</p>
      </article>
      <article class="menu-item">
        <div class="item-head"><h3 class="item-name">GLO</h3><svg class="item-leader" viewBox="0 0 100 14" preserveAspectRatio="none"><path d="M0 13 H80 L88 1 H100" fill="none" stroke="var(--purple)" stroke-width="1" vector-effect="non-scaling-stroke"/></svg><span class="item-price">$200</span></div>
        <p class="item-desc">A Beauty mixture of Glutathione, Biotin and our special formula created to strengthen your hair, nails and skin for that SPECIAL LOOK!</p>
      </article>
      <article class="menu-item">
        <div class="item-head"><h3 class="item-name">THE ULTIMATE WEIGHT<br>LOSS INFUSION</h3><svg class="item-leader" viewBox="0 0 100 14" preserveAspectRatio="none"><path d="M0 13 H60 L80 1 H100" fill="none" stroke="var(--purple)" stroke-width="1" vector-effect="non-scaling-stroke"/></svg><span class="item-price">$180</span></div>
        <p class="item-desc">Our unique fat burning formula targets fatty deposits resulting in fat expulsion from the body resulting in a more defined and contoured appearance.</p>
      </article>
      <article class="menu-item">
        <div class="item-head"><h3 class="item-name">NAD+ IV: THE FOUNTAIN<br>OF YOUTH (+-)</h3><svg class="item-leader" viewBox="0 0 100 14" preserveAspectRatio="none"><path d="M0 13 H60 L80 1 H100" fill="none" stroke="var(--purple)" stroke-width="1" vector-effect="non-scaling-stroke"/></svg><span class="item-price">$350</span></div>
        <p class="item-desc">Anti-aging co-enzyme NAD+ in conjunction with Vitamins elevates brain health and beauty, all in one IV treatment!</p>
      </article>
    </div>
  </div>

  <div class="vitamin-panel">
    <h2 class="vit-title">DR. VERANO'S</h2>
    <p class="vit-banner">VITAMIN B12 COCKTAIL'S<br>ESSENTIAL VITAMINS &amp; NUTRIENTS:</p>
    <ul class="nutrients">
      <li class="nutrient"><svg width="9" height="9" viewBox="0 0 10 10"><circle cx="5" cy="5" r="4.3" fill="none" stroke="var(--purple)" stroke-width=".9"/><path d="M3 5.1l1.4 1.4L7 3.8" fill="none" stroke="var(--purple)" stroke-width=".9"/></svg><span><b>Thiamine -</b> is used by the body to metabolize food for energy and maintain proper health and nerve function.</span></li>
      <li class="nutrient"><svg width="9" height="9" viewBox="0 0 10 10"><circle cx="5" cy="5" r="4.3" fill="none" stroke="var(--purple)" stroke-width=".9"/><path d="M3 5.1l1.4 1.4L7 3.8" fill="none" stroke="var(--purple)" stroke-width=".9"/></svg><span><b>Riboflavin -</b> acts as an antioxidant within the body. Riboflavin prevents free radical damage and protects skin and eye health.</span></li>
      <li class="nutrient"><svg width="9" height="9" viewBox="0 0 10 10"><circle cx="5" cy="5" r="4.3" fill="none" stroke="var(--purple)" stroke-width=".9"/><path d="M3 5.1l1.4 1.4L7 3.8" fill="none" stroke="var(--purple)" stroke-width=".9"/></svg><span><b>Niacinamide -</b> helps maintain a healthy cardiovascular system and metabolism, brain function, healthy skin formation, and aids in the prevention of and management of diabetes.</span></li>
      <li class="nutrient"><svg width="9" height="9" viewBox="0 0 10 10"><circle cx="5" cy="5" r="4.3" fill="none" stroke="var(--purple)" stroke-width=".9"/><path d="M3 5.1l1.4 1.4L7 3.8" fill="none" stroke="var(--purple)" stroke-width=".9"/></svg><span><b>Pyridoxine -</b> is important for brain development and keeping the nervous and immune systems healthy.</span></li>
      <li class="nutrient"><svg width="9" height="9" viewBox="0 0 10 10"><circle cx="5" cy="5" r="4.3" fill="none" stroke="var(--purple)" stroke-width=".9"/><path d="M3 5.1l1.4 1.4L7 3.8" fill="none" stroke="var(--purple)" stroke-width=".9"/></svg><span><b>Hydroxocobalamin -</b> helps with DNA synthesis and supports replication, it also helps in the body's use of fats and carbohydrates for energy, and in the making of new proteins.</span></li>
      <li class="nutrient"><svg width="9" height="9" viewBox="0 0 10 10"><circle cx="5" cy="5" r="4.3" fill="none" stroke="var(--purple)" stroke-width=".9"/><path d="M3 5.1l1.4 1.4L7 3.8" fill="none" stroke="var(--purple)" stroke-width=".9"/></svg><span><b>Methionine -</b> aids in tissue growth and repair, as well as promoting healthy hair, skin, and nails.</span></li>
      <li class="nutrient"><svg width="9" height="9" viewBox="0 0 10 10"><circle cx="5" cy="5" r="4.3" fill="none" stroke="var(--purple)" stroke-width=".9"/><path d="M3 5.1l1.4 1.4L7 3.8" fill="none" stroke="var(--purple)" stroke-width=".9"/></svg><span><b>Inositol -</b> aids in the metabolic breakdown of fats, and helps reduce blood cholesterol.</span></li>
      <li class="nutrient"><svg width="9" height="9" viewBox="0 0 10 10"><circle cx="5" cy="5" r="4.3" fill="none" stroke="var(--purple)" stroke-width=".9"/><path d="M3 5.1l1.4 1.4L7 3.8" fill="none" stroke="var(--purple)" stroke-width=".9"/></svg><span><b>L-carnitine -</b> helps convert fatty acids into energy.</span></li>
      <li class="nutrient"><svg width="9" height="9" viewBox="0 0 10 10"><circle cx="5" cy="5" r="4.3" fill="none" stroke="var(--purple)" stroke-width=".9"/><path d="M3 5.1l1.4 1.4L7 3.8" fill="none" stroke="var(--purple)" stroke-width=".9"/></svg><span><b>Chromium -</b> helps move sugars from the blood system, and turn fats, carbs, and proteins into energy.</span></li>
    </ul>

    <div class="benefits-head">
      <h3 class="benefits-title">OVERALL BENEFITS:</h3>
      <svg class="item-leader" viewBox="0 0 100 14" preserveAspectRatio="none"><path d="M0 13 H20 L30 1 H100" fill="none" stroke="var(--purple)" stroke-width="1" vector-effect="non-scaling-stroke"/></svg>
    </div>
    <ul class="benefits">
      <li class="benefit"><svg width="8" height="8" viewBox="0 0 10 10"><path d="M1 5.5l2.6 2.6L9 1.8" fill="none" stroke="var(--purple)" stroke-width="1.3"/></svg><span>B12 helps aid in red blood cell formation and in DNA synthesis</span></li>
      <li class="benefit"><svg width="8" height="8" viewBox="0 0 10 10"><path d="M1 5.5l2.6 2.6L9 1.8" fill="none" stroke="var(--purple)" stroke-width="1.3"/></svg><span>Aids in the healthy maintenance of the immune and nervous systems, and the optic nerve</span></li>
      <li class="benefit"><svg width="8" height="8" viewBox="0 0 10 10"><path d="M1 5.5l2.6 2.6L9 1.8" fill="none" stroke="var(--purple)" stroke-width="1.3"/></svg><span>Helps improve skin tone, and strengthen nails and hair</span></li>
      <li class="benefit"><svg width="8" height="8" viewBox="0 0 10 10"><path d="M1 5.5l2.6 2.6L9 1.8" fill="none" stroke="var(--purple)" stroke-width="1.3"/></svg><span>Boosts metabolism and energy (which may help reduce craving and encourage weight loss)</span></li>
      <li class="benefit"><svg width="8" height="8" viewBox="0 0 10 10"><path d="M1 5.5l2.6 2.6L9 1.8" fill="none" stroke="var(--purple)" stroke-width="1.3"/></svg><span>Helps relieve cramping and bloating</span></li>
      <li class="benefit"><svg width="8" height="8" viewBox="0 0 10 10"><path d="M1 5.5l2.6 2.6L9 1.8" fill="none" stroke="var(--purple)" stroke-width="1.3"/></svg><span>Improves memory (which may protect against Alzheimer's)</span></li>
      <li class="benefit"><svg width="8" height="8" viewBox="0 0 10 10"><path d="M1 5.5l2.6 2.6L9 1.8" fill="none" stroke="var(--purple)" stroke-width="1.3"/></svg><span>Enhances mood and lessens the effects of depression</span></li>
    </ul>
  </div>
</section>

</body>
</html>
```